Real Estate Open House A Frame Sign

The sign is 22" wide and 28" tall. This sign is used to post around the neighbourhood to direct people to an open house (home that is for sale). It is also used for self-promotion.

Designwise
- I just want something with a modern look, simple and clean.
- I want my picture and business logo on the left side.
- On the right side, website (www.lumwick-realestate.com) and my phone (555-374-9126), then a blank space where I can write an address when I need to.

I'm not sure how I want the overall design look. I'm very open-minded and I'm depending on your creative mind to come up with something.

If you have any questions, please let me know.

```html
<!DOCTYPE html>
<html lang="en">
<head>
<meta charset="utf-8">
<title>Lumwick Real Estate – Open House Sign</title>
<link rel="stylesheet" href="https://fonts.googleapis.com/css2?family=Montserrat:wght@300;500;600;700;800&display=swap">
<style>
  :root {
    --page-bg: #eef0f2;
    --slate: #4d5056;
    --navy: #0a4382;
    --white: #ffffff;
    --signal-yellow: #f2e614;
    --portrait-top: #6a6d74;
    --portrait-bottom: #23262c;
  }
  * { box-sizing: border-box; margin: 0; padding: 0; }
  html, body {
    width: 1066px; height: 1200px; overflow: hidden;
    background: var(--page-bg);
    font-family: "Montserrat", sans-serif;
  }
  .sign {
    position: absolute; left: 101px; top: 50px;
    width: 864px; height: 1100px;
    border-radius: 22px; overflow: hidden;
    background: var(--navy);
    box-shadow: 0 10px 30px rgba(0,0,0,0.18);
  }
  .brand-panel {
    position: absolute; left: 0; top: 0; width: 100%; height: 460px;
    background: var(--slate);
  }
  .brand-name {
    position: absolute; left: 112px; top: 175px;
    color: var(--white); font-weight: 300;
    line-height: 1;
  }
  .brand-name .word {
    display: block; font-size: 66px; letter-spacing: 4px;
  }
  .brand-name .tagline {
    display: block; margin-top: 22px; font-size: 29px; letter-spacing: 9px;
  }
  .agent-portrait {
    position: absolute; right: 20px; bottom: 0;
    width: 250px; height: 360px;
    border-radius: 120px 120px 0 0;
    background: linear-gradient(180deg, var(--portrait-top), var(--portrait-bottom));
  }
  .open-panel {
    position: absolute; left: 0; top: 460px; width: 100%; height: 415px;
    background: var(--navy); color: var(--white); text-align: center;
  }
  .hosted-label {
    position: absolute; left: 0; right: 0; top: 44px;
    font-size: 26px; font-weight: 600; letter-spacing: 7px;
  }
  .agent-name {
    position: absolute; left: 0; right: 0; top: 84px;
    font-size: 64px; font-weight: 800; letter-spacing: 6px;
  }
  .open-line {
    position: absolute; left: 50px; right: 30px; top: 178px;
    display: flex; align-items: center; justify-content: center; gap: 26px;
  }
  .open-word {
    font-size: 132px; font-weight: 800; letter-spacing: 18px; line-height: 1;
  }
  .direction-arrow { width: 96px; height: 96px; flex: none; }
  .phone {
    position: absolute; left: 0; right: 0; top: 322px;
    font-size: 56px; font-weight: 700; letter-spacing: 4px;
  }
  .address-space {
    position: absolute; left: 0; top: 875px; width: 100%; height: 126px;
    background: var(--white);
  }
  .footer-panel {
    position: absolute; left: 0; top: 1001px; width: 100%; height: 99px;
    background: var(--navy); color: var(--white); text-align: center;
  }
  .website {
    margin-top: 18px; font-size: 32px; font-weight: 700; letter-spacing: 3px;
  }
  .licence {
    margin-top: 6px; font-size: 24px; font-weight: 600; letter-spacing: 1px;
  }
</style>
</head>
<body>
  <main class="sign">
    <section class="brand-panel">
      <div class="brand-name">
        <span class="word">LUMWICK</span>
        <span class="tagline">REAL ESTATE</span>
      </div>
      <div class="agent-portrait" role="img" aria-label="Portrait photo of the agent in a dark suit, arms crossed"></div>
    </section>

    <section class="open-panel">
      <p class="hosted-label">HOSTED BY</p>
      <h1 class="agent-name">DAN HOLLIS</h1>
      <div class="open-line">
        <span class="open-word">OPEN</span>
        <svg class="direction-arrow" viewBox="0 0 96 96" aria-hidden="true">
          <circle cx="48" cy="48" r="46" fill="var(--signal-yellow)"/>
          <path d="M26 48 H66 M50 31 L68 48 L50 65" fill="none" stroke="var(--navy)" stroke-width="8" stroke-linecap="round" stroke-linejoin="round"/>
        </svg>
      </div>
      <p class="phone">555-374-9126</p>
    </section>

    <section class="address-space" aria-label="Blank space for handwritten address"></section>

    <footer class="footer-panel">
      <p class="website">LUMWICK-REALESTATE.COM</p>
      <p class="licence">DRE #04478215</p>
    </footer>
  </main>
</body>
</html>
```